Business Card Design Project

We are a commercial talent casting company, a very "now" company. We need a new business card that is both current, graphic and elegantly interesting. As we are a service business,
we need something that will attract the attention of new clients,
yet project a business that is 25 years old.

Industry/Entity Type

Business

Requirements
Must have
• 1. Logo - Nora Quillan Casting
2. Address - 47 Harwick Street
New York, New York 10027
3. Phone - 212-638-4170
4. E-Mail - Casting@noraquillan.com

Nice to have
• Would like the card in black and white with the only accent
color being red.

```html
<!DOCTYPE html>
<html lang="en">
<head>
<meta charset="utf-8">
<title>Nora Quillan Casting – Business Cards</title>
<link rel="stylesheet" href="https://fonts.googleapis.com/css2?family=Oswald:wght@600&family=Open+Sans:wght@400;600&display=swap">
<style>
  :root {
    --stage: #6b4429;
    --card-white: #ffffff;
    --card-black: #000000;
    --card-red: #c8161d;
    --red-band: #c8161d;
    --ink: #111111;
    --ink-soft: #555555;
    --paper-text: #ffffff;
    --ornament: #f1f1f1;
    --mark-dot: #c8161d;
  }
  * { margin: 0; padding: 0; box-sizing: border-box; }
  html, body { width: 1200px; height: 754px; overflow: hidden; }
  body {
    background: var(--stage);
    position: relative;
    font-family: "Open Sans", Arial, sans-serif;
  }
  .card {
    position: absolute;
    width: 528px;
    height: 302px;
    border-radius: 20px;
    overflow: hidden;
  }
  .card--front { left: 318px; top: 40px; background: var(--card-white); }
  .card--back-black { left: 62px; top: 380px; background: var(--card-black); }
  .card--back-red { left: 623px; top: 372px; background: var(--card-red); }

  .front__band {
    position: absolute; left: 0; top: 0; bottom: 0; width: 62px;
    background: var(--red-band);
    border-right: 4px solid var(--ink);
  }
  .front__icons {
    position: absolute; left: 38px; bottom: 10px;
    display: flex; flex-direction: column; gap: 6px;
  }
  .front__ornament {
    position: absolute; left: 200px; top: 120px; width: 328px; height: 182px;
    background: radial-gradient(ellipse at 60% 60%, var(--ornament), rgba(255,255,255,0) 70%);
  }

  .wordmark {
    position: absolute;
    display: flex; align-items: center; gap: 10px;
    font-family: "Oswald", "Arial Narrow", sans-serif;
    font-weight: 600;
    text-transform: uppercase;
    line-height: 1;
    letter-spacing: 0.5px;
  }
  .wordmark__dot {
    width: 18px; height: 18px; border-radius: 50%;
    background: var(--mark-dot); flex: none;
  }
  .wordmark__text { font-size: 34px; }
  .wordmark__sub { display: block; font-size: 22px; margin-top: 4px; letter-spacing: 4px; }

  .card--front .wordmark { left: 76px; top: 108px; color: var(--ink); }
  .card--back-black .wordmark { left: 136px; top: 150px; color: var(--paper-text); }
  .card--back-red .wordmark { left: 136px; top: 152px; color: var(--paper-text); }
  .card--back-black .wordmark__dot,
  .card--back-red .wordmark__dot { background: var(--paper-text); }

  .front__contact {
    position: absolute; left: 74px; top: 220px;
    font-size: 13px; line-height: 18.5px; color: var(--ink);
  }
  .front__contact .gap { margin-top: 2px; }
  .front__person {
    position: absolute; left: 300px; top: 230px; color: var(--ink-soft);
  }
  .front__name { font-size: 18px; font-weight: 600; color: #333; }
  .front__role { font-size: 11.5px; letter-spacing: 2.5px; margin-top: 2px; }
</style>
</head>
<body>

  <section class="card card--front" aria-label="Card front">
    <div class="front__band">
      <div class="front__icons">
        <svg width="14" height="14" viewBox="0 0 24 24" aria-label="Phone"><path fill="#fff" d="M6.6 10.8a15.5 15.5 0 0 0 6.6 6.6l2.2-2.2c.3-.3.7-.4 1-.2 1.1.4 2.3.6 3.6.6.6 0 1 .4 1 1V20c0 .6-.4 1-1 1A17 17 0 0 1 3 4c0-.6.4-1 1-1h3.5c.6 0 1 .4 1 1 0 1.3.2 2.5.6 3.6.1.3 0 .7-.2 1z"/></svg>
        <svg width="15" height="12" viewBox="0 0 24 18" aria-label="Email"><rect x="1" y="1" width="22" height="16" fill="none" stroke="#fff" stroke-width="2"/><path d="M1 1l11 9 11-9" fill="none" stroke="#fff" stroke-width="2"/></svg>
      </div>
    </div>
    <div class="front__ornament" role="img" aria-label="Faint floral swirl ornament"></div>
    <div class="wordmark">
      <span class="wordmark__text">Nora Quillan<span class="wordmark__sub">Casting</span></span>
      <span class="wordmark__dot"></span>
    </div>
    <address class="front__contact" style="font-style:normal">
      47 Harwick Street<br>
      New York, New York 10027<br>
      <span class="gap">212-638-4170</span><br>
      Casting@noraquillan.com
    </address>
    <div class="front__person">
      <div class="front__name">YOUR NAME HERE</div>
      <div class="front__role">DIRECTOR</div>
    </div>
  </section>

  <section class="card card--back-black" aria-label="Card back, black">
    <div class="wordmark">
      <span class="wordmark__text">Nora Quillan<span class="wordmark__sub">Casting</span></span>
      <span class="wordmark__dot"></span>
    </div>
  </section>

  <section class="card card--back-red" aria-label="Card back, red">
    <div class="wordmark">
      <span class="wordmark__text">Nora Quillan<span class="wordmark__sub">Casting</span></span>
      <span class="wordmark__dot"></span>
    </div>
  </section>

</body>
</html>
```